AUSTRALIAN CONSULTING FIRM BUSINESS CARD - MODERN

We are wanting a modern, clean lined business card design. We are professional niche consultancy firm situated in Australia called Marlow Advisory Partners Pty Ltd.
The card should communicate professionalism and creativity and draw on our logo design (attached).
The design should be two sided, landscape orientation.
Target Market(s)
government, not for profit sector, corporate clients
Industry/Entity Type
Landscape
Requirements
Must have
- logo
no new introduced colours

```html
<!DOCTYPE html>
<html lang="en">
<head>
<meta charset="utf-8">
<title>Marlow Advisory Partners – Business Card</title>
<link href="https://fonts.googleapis.com/css2?family=Fira+Sans:wght@400;500;700&display=swap" rel="stylesheet">
<style>
  :root {
    --stage: #d4d4d4;
    --navy: #1a4599;
    --sky: #1aa1e0;
    --magenta: #a3288f;
    --lime: #8cc63f;
    --ink-soft: #8a8a8a;
    --paper: #ffffff;
  }
  * { margin: 0; padding: 0; box-sizing: border-box; }
  html, body { width: 1200px; height: 902px; overflow: hidden; }
  body {
    background: var(--stage);
    font-family: "Fira Sans", sans-serif;
    position: relative;
  }
  .card {
    position: absolute;
    left: 299px;
    width: 600px;
    height: 342px;
    border-radius: 22px;
    overflow: hidden;
  }
  .card--front { top: 89px; background: var(--navy); }
  .card--back  { top: 459px; height: 340px; background: var(--paper); }

  .emblem-area {
    position: absolute;
    left: 32px;
    top: 8px;
    width: 304px;
    height: 326px;
    border-radius: 24px;
    background: linear-gradient(160deg, rgba(26,161,224,0.55) 0%, rgba(163,40,143,0.45) 50%, rgba(140,198,63,0.5) 100%);
  }

  .front-brand {
    position: absolute;
    right: 54px;
    top: 272px;
    display: flex;
    align-items: center;
    gap: 10px;
  }
  .brand-dot { width: 16px; height: 16px; border-radius: 50%; background: var(--sky); flex: none; }
  .front-brand .brand-name {
    color: var(--paper);
    font-weight: 700;
    font-size: 19px;
    letter-spacing: 0.2px;
  }

  .holder { position: absolute; right: 36px; top: 28px; text-align: right; line-height: 1.05; }
  .holder-name { color: var(--magenta); font-weight: 500; font-size: 28px; }
  .holder-role { color: var(--lime); font-weight: 500; font-size: 22px; }

  .back-brand {
    position: absolute;
    left: 27px;
    top: 134px;
    display: flex;
    align-items: center;
    gap: 10px;
  }
  .back-brand .brand-name { color: var(--navy); font-weight: 700; font-size: 19px; }

  .address {
    position: absolute;
    left: 45px;
    top: 213px;
    color: var(--ink-soft);
    font-size: 14px;
    line-height: 17px;
  }
  .rule {
    position: absolute;
    left: 43px;
    top: 256px;
    width: 313px;
    height: 2px;
    background: var(--lime);
  }
  .website {
    position: absolute;
    right: 36px;
    top: 246px;
    color: var(--navy);
    font-size: 15px;
    font-weight: 500;
    letter-spacing: 1px;
  }
  .contacts {
    position: absolute;
    left: 43px;
    top: 270px;
    display: grid;
    grid-template-columns: 178px auto;
    row-gap: 7px;
    color: var(--ink-soft);
    font-size: 14px;
  }
  .contact { display: flex; align-items: center; gap: 7px; height: 18px; }
  .contact-icon { width: 18px; height: 18px; flex: none; }
</style>
</head>
<body>
  <section class="card card--front" aria-label="Card front">
    <div class="emblem-area" role="img" aria-label="Large company emblem area"></div>
    <div class="front-brand">
      <span class="brand-dot"></span>
      <span class="brand-name">Marlow Advisory Partners Pty Ltd</span>
    </div>
  </section>

  <section class="card card--back" aria-label="Card back">
    <div class="holder">
      <div class="holder-name">Daniel Hartley</div>
      <div class="holder-role">Director</div>
    </div>

    <div class="back-brand">
      <span class="brand-dot"></span>
      <span class="brand-name">Marlow Advisory Partners Pty Ltd</span>
    </div>

    <div class="address">
      Marlow Advisory Partners PTY LTD<br>
      Your Office, AB 12345
    </div>

    <div class="rule"></div>
    <div class="website">www.marlowadvisory.com</div>

    <div class="contacts">
      <div class="contact">
        <svg class="contact-icon" viewBox="0 0 18 18" aria-hidden="true">
          <circle cx="9" cy="9" r="9" fill="var(--navy)"/>
          <path d="M6 4.5c.6 0 1.4 1.6 1.4 2.2 0 .5-.8.8-.7 1.3.3 1 1.3 2 2.3 2.3.5.1.8-.7 1.3-.7.6 0 2.2.8 2.2 1.4 0 .9-1 1.8-2 1.6C7.8 12.1 5.9 10.2 5.4 7.5 5.2 6.4 5.1 4.5 6 4.5z" fill="#fff"/>
        </svg>
        <span>780-555-0192</span>
      </div>
      <div class="contact">
        <svg class="contact-icon" viewBox="0 0 18 18" aria-hidden="true">
          <circle cx="9" cy="9" r="9" fill="var(--navy)"/>
          <rect x="4.5" y="6" width="9" height="6.5" fill="#fff"/>
          <path d="M4.5 6l4.5 3.6L13.5 6" fill="none" stroke="var(--navy)" stroke-width="1"/>
        </svg>
        <span>info@marlowadvisory.com</span>
      </div>
      <div class="contact">
        <svg class="contact-icon" viewBox="0 0 18 18" aria-hidden="true">
          <circle cx="9" cy="9" r="9" fill="var(--navy)"/>
          <path d="M4.5 5.5h9v5.5h-5l-2.5 2v-2h-1.5z" fill="#fff"/>
        </svg>
        <span>@marlowadvisory</span>
      </div>
      <div class="contact">
        <svg class="contact-icon" viewBox="0 0 18 18" aria-hidden="true">
          <circle cx="9" cy="9" r="9" fill="var(--navy)"/>
          <circle cx="9" cy="9" r="4.3" fill="none" stroke="#fff" stroke-width="1.2"/>
          <path d="M4.7 9h8.6M9 4.7c-1.6 1.4-1.6 7.2 0 8.6M9 4.7c1.6 1.4 1.6 7.2 0 8.6" fill="none" stroke="#fff" stroke-width="1"/>
        </svg>
        <span>/marlowadvisory</span>
      </div>
    </div>
  </section>
</body>
</html>
```